Online Rug Store needs Clearance Banner

Website is: Lanternfield Carpets and Home
You can access it at: www.lanternfieldcarpetsandhome.com and login (top right) with password: trazok

*** update: When creating banners for my site, you have permission to use images from www.velbora.com, but ONLY for this project. The images/artwork are copyright allowable for use on www.lanternfieldcarpetsandhome.com projects.***

We need a home page banner sized 1000 wide x 500 tall pixels to promote a "Clearance Sale" on rugs. The banner can state:

1. Clearance Sale
2. Now in progress
3. Save an extra 20% with coupon code 'Mint20'
4. Ends March 31st
5. Plus Free Shipping and 30 day returns.

We prefer a banner that appears hand-drawn and artistic, not commercially produced. It is OK to use a room scene image, rug images, or just a colored/textured background with text and no images. Your choice.

Flat graphics with no shadows and 3-D effect preferred.
Attached is are 3 logo options, as well as an example banner with handcrafted, artistic styling that we prefer.

Target Market(s)

This should be an eye-catching banner to showcase a very urgent promotion. Consider using colors of red, white, gold, and black to make a strong statement on the home page.

Industry/Entity Type

Home And Garden

Requirements
Must have
• Winner must provide Photoshop editable file format (.psd format) including layers that can be edited.
Nice to have
• Hand-drawn, stenciled, scribbled, artistic graphics and fonts is nice because we sell rugs that are made by hand.
Should not have
• little to no shadowing. Avoid computerized graphics.

```html
<!DOCTYPE html>
<html lang="en">
<head>
<meta charset="utf-8">
<title>Clearance Sale Banner – Lanternfield Carpets and Home</title>
<link rel="stylesheet" href="https://fonts.googleapis.com/css2?family=Great+Vibes&family=Kaushan+Script&display=swap">
<style>
  :root {
    --stage: #e4e4e4;
    --raspberry: #c41a5a;
    --raspberry-deep: #a3124a;
    --raspberry-shade: #7e0c38;
    --camel: #d6a86c;
    --camel-light: #e2bd86;
    --paisley-a: #c9a26a;
    --paisley-b: #b59a6c;
    --paisley-c: #d8b47c;
    --ink: #111111;
    --chalk: #ffffff;
    --script: "Great Vibes", cursive;
    --hand: "Kaushan Script", cursive;
  }
  * { margin: 0; padding: 0; box-sizing: border-box; }
  html, body {
    width: 1200px;
    height: 688px;
    overflow: hidden;
    background: var(--stage);
  }
  .banner {
    position: absolute;
    left: 100px;
    top: 94px;
    width: 1000px;
    height: 500px;
    overflow: hidden;
    background: var(--camel);
  }
  .headline-band {
    position: absolute;
    left: 0; top: 0;
    width: 1000px; height: 233px;
    background: radial-gradient(ellipse at 40% 40%, #cc2262 0%, var(--raspberry) 55%, var(--raspberry-deep) 100%);
  }
  .headline {
    position: absolute;
    left: 122px; top: 22px;
    font-family: var(--script);
    font-weight: 400;
    font-size: 158px;
    line-height: 1;
    color: var(--chalk);
    white-space: nowrap;
    letter-spacing: 1px;
  }
  .status {
    position: absolute;
    left: 128px; top: 170px;
    font-family: var(--hand);
    font-size: 40px;
    color: var(--ink);
    white-space: nowrap;
  }
  .deadline {
    position: absolute;
    left: 682px; top: 176px;
    font-family: var(--hand);
    font-size: 26px;
    color: var(--chalk);
    white-space: nowrap;
  }
  .deadline sup { font-size: 15px; vertical-align: 12px; }
  .offer-band {
    position: absolute;
    left: 0; top: 233px;
    width: 1000px; height: 94px;
    background: var(--camel);
  }
  .offer {
    position: absolute;
    left: 110px; top: 22px;
    font-family: var(--hand);
    font-size: 38px;
    color: var(--chalk);
    white-space: nowrap;
  }
  .offer .amount { color: var(--ink); }
  .coupon {
    position: absolute;
    left: 796px; top: 10px;
    width: 196px; height: 72px;
    border: 2px dashed var(--raspberry);
    background: var(--camel-light);
    font-family: var(--hand);
    font-size: 44px;
    color: var(--ink);
    display: flex;
    align-items: center;
    justify-content: center;
  }
  .pattern-field {
    position: absolute;
    left: 0; top: 327px;
    width: 1000px; height: 173px;
    background:
      radial-gradient(circle at 20% 50%, var(--paisley-b) 0%, transparent 40%),
      radial-gradient(circle at 55% 60%, var(--paisley-b) 0%, transparent 35%),
      radial-gradient(circle at 85% 40%, var(--paisley-b) 0%, transparent 35%),
      linear-gradient(180deg, var(--paisley-c), var(--paisley-a));
  }
  .ribbon {
    position: absolute;
    width: 360px; height: 120px;
  }
  .ribbon svg { position: absolute; left: 0; top: 0; }
  .ribbon-shipping { left: 14px; top: 356px; }
  .ribbon-returns { left: 634px; top: 356px; }
  .ribbon-label {
    position: absolute;
    font-family: var(--hand);
    color: var(--ink);
    white-space: nowrap;
    text-align: center;
  }
  .ribbon-shipping .ribbon-label {
    left: 60px; top: 22px;
    font-size: 32px;
  }
  .ribbon-shipping .ribbon-label .lead { color: var(--chalk); }
  .ribbon-returns .ribbon-label {
    left: 60px; top: 4px;
    width: 280px;
    font-size: 32px;
    line-height: 36px;
  }
</style>
</head>
<body>
  <main class="banner">
    <section class="headline-band">
      <h1 class="headline">Clearance Sale</h1>
      <p class="status">Now in progress</p>
      <p class="deadline">Ends March 31<sup>st</sup></p>
    </section>

    <section class="offer-band">
      <p class="offer">Save an extra <span class="amount">20%</span> with coupon code</p>
      <div class="coupon">Mint20</div>
    </section>

    <div class="pattern-field" role="img" aria-label="Paisley rug pattern in gold, olive and rust tones"></div>

    <div class="ribbon ribbon-shipping">
      <svg width="360" height="120" viewBox="0 0 360 120">
        <polygon points="20,68 74,68 74,108" fill="var(--raspberry-shade)"/>
        <path d="M56,4 H318 Q332,4 328,18 L314,58 Q310,68 296,68 H20 Z" fill="var(--raspberry)"/>
      </svg>
      <p class="ribbon-label"><span class="lead">FREE</span> SHIPPING</p>
    </div>

    <div class="ribbon ribbon-returns">
      <svg width="360" height="120" viewBox="0 0 360 120">
        <polygon points="56,60 112,60 112,100" fill="var(--raspberry-shade)"/>
        <path d="M96,4 H338 Q352,4 348,18 L336,58 Q332,74 318,74 H56 Z" fill="var(--raspberry)"/>
      </svg>
      <p class="ribbon-label">30<br>DAY RETURNS</p>
    </div>
  </main>
</body>
</html>
```